Yoga for Scoliosis business card/logo design

I need a business card/logo design for my new business. I am a registered yoga teacher and am certified in yoga for scoliosis. I'd like my card to read "Marlow Yoga Yoga for a Healthy Spine" and would like to incorporate one of the letters in my name{ ie the first vertical line of the letter " H "or "D"} to resemble a scoliotic spine. I regularly teach the following:Yoga for Scoliosis, Yoga for Back Health, Hatha yoga, Vinyasa yoga with Iyengar style alignment. This business is mostly for private clients, but I also teach group, semi-private & work shop classes. I like the colors green (light emerald) and royal blue. I'd like the design to be somewhat sleek, but not too modern. I also like the idea of a ying/yang symbol with a scoliotic spine dviding it.

Industry/Entity Type

Teacher

Contact Information for Business Card

Tamsin Marlow
200 RYT, Certified Yoga for Scoliosis Instructor
MarlowYoga.example
MarlowYoga@mailbox.example
415-629-3174

```html
<!DOCTYPE html>
<html lang="en">
<head>
<meta charset="utf-8">
<title>Marlow Yoga — Business Card</title>
<link href="https://fonts.googleapis.com/css2?family=Arimo:wght@400&family=Dancing+Script:wght@500&family=Montserrat:wght@500&display=swap" rel="stylesheet">
<style>
  :root {
    --page-bg: #ffffff;
    --royal-blue: #21508f;
    --deep-blue: #123a73;
    --back-blue-light: #1d5aa3;
    --emerald: #0a9a72;
    --emerald-text: #1fa36b;
    --silver: #c8ccd3;
    --silver-line: #9ea6b3;
    --white: #ffffff;
  }
  * { box-sizing: border-box; margin: 0; padding: 0; }
  html, body { width: 1200px; height: 800px; overflow: hidden; background: var(--page-bg); }
  .canvas {
    position: relative; width: 1200px; height: 800px;
    display: flex; align-items: center; justify-content: center; gap: 40px;
  }
  .card {
    position: relative; width: 540px; height: 309px;
    border-radius: 22px; overflow: hidden;
    box-shadow: 0 6px 18px rgba(0,0,0,0.28);
  }

  /* Front */
  .card--front { background: var(--royal-blue); }
  .card__accent {
    position: absolute; inset: 0; width: 100%; height: 100%;
  }
  .brand {
    position: absolute; display: flex; align-items: center; gap: 14px;
    font-family: "Montserrat", sans-serif; font-weight: 500;
    color: var(--silver); letter-spacing: 0.02em;
  }
  .brand__mark {
    display: block; border-radius: 50%; background: var(--silver);
  }
  .card--front .brand { left: 34px; top: 52px; font-size: 30px; }
  .card--front .brand__mark { width: 58px; height: 58px; }
  .divider {
    position: absolute; left: 184px; top: 138px; width: 2px; height: 140px;
    background: var(--emerald-text);
  }
  .contact {
    position: absolute; left: 202px; top: 132px; color: var(--white);
    font-family: "Arimo", sans-serif;
  }
  .contact__name {
    font-family: "Dancing Script", cursive; font-weight: 500;
    color: var(--emerald-text); font-size: 32px; line-height: 1; margin-bottom: 6px;
  }
  .contact__title { font-size: 12px; margin-bottom: 8px; white-space: nowrap; }
  .contact__list { list-style: none; }
  .contact__item {
    display: flex; align-items: center; gap: 9px;
    font-size: 15px; line-height: 23px; white-space: nowrap;
  }
  .contact__icon { width: 13px; height: 13px; flex: none; }

  /* Back */
  .card--back {
    background: radial-gradient(ellipse at 55% 40%, var(--back-blue-light) 0%, var(--deep-blue) 75%);
  }
  .card--back .brand {
    left: 0; right: 0; top: 82px; justify-content: center; font-size: 40px; gap: 18px;
  }
  .card--back .brand__mark { width: 84px; height: 84px; }
  .services {
    position: absolute; left: 0; right: 0; bottom: 46px; text-align: center;
    font-family: "Montserrat", sans-serif; font-weight: 500; color: var(--white);
    font-size: 10.5px; letter-spacing: 0.22em; text-transform: uppercase; line-height: 20px;
  }
</style>
</head>
<body>
<main class="canvas">

  <section class="card card--front" aria-label="Business card front">
    <svg class="card__accent" viewBox="0 0 540 309" preserveAspectRatio="none" aria-hidden="true">
      <polygon points="450,309 540,210 540,309" fill="var(--emerald)"/>
      <line x1="450" y1="309" x2="540" y2="210" stroke="var(--silver-line)" stroke-width="2"/>
    </svg>
    <div class="brand">
      <span class="brand__mark" aria-hidden="true"></span>
      <span class="brand__name">Marlow Yoga</span>
    </div>
    <div class="divider" aria-hidden="true"></div>
    <div class="contact">
      <p class="contact__name">Tamsin Marlow</p>
      <p class="contact__title">200 RYT, Certified Yoga for Scoliosis Instructor</p>
      <ul class="contact__list">
        <li class="contact__item">
          <svg class="contact__icon" viewBox="0 0 16 16" aria-hidden="true"><path fill="#fff" d="M3 1h3l1.5 4-2 1.2a9 9 0 0 0 4.3 4.3L11 8.5l4 1.5v3a2 2 0 0 1-2 2A12 12 0 0 1 1 3a2 2 0 0 1 2-2z"/></svg>
          415-629-3174
        </li>
        <li class="contact__item">
          <svg class="contact__icon" viewBox="0 0 16 16" aria-hidden="true"><g fill="none" stroke="#fff" stroke-width="1.3"><circle cx="8" cy="8" r="6.5"/><ellipse cx="8" cy="8" rx="2.8" ry="6.5"/><line x1="1.5" y1="8" x2="14.5" y2="8"/></g></svg>
          MarlowYoga.example
        </li>
        <li class="contact__item">
          <svg class="contact__icon" viewBox="0 0 16 16" aria-hidden="true"><rect x="1" y="3" width="14" height="10" fill="#fff"/><path d="M1 3l7 6 7-6" fill="none" stroke="var(--royal-blue)" stroke-width="1.2"/></svg>
          MarlowYoga@mailbox.example
        </li>
      </ul>
    </div>
  </section>

  <section class="card card--back" aria-label="Business card back">
    <div class="brand">
      <span class="brand__mark" aria-hidden="true"></span>
      <span class="brand__name">Marlow Yoga</span>
    </div>
    <div class="services">
      <p>Yoga for Scoliosis | Yoga for Back Health | Hatha Yoga</p>
      <p>Vinyasa Yoga with Iyengar Style Alignment</p>
    </div>
  </section>

</main>
</body>
</html>
```